Wordpress website for a new Podcast

Hi, We are looking for a designer to create a wordpress website project for a new podcast and publish it on the domain we own.

The show is called “Bright Huddles” (logo included) and its aim is to interview guests who work as professional facilitators, trainers, teachers and coaches. The show has a positive vibe, is fun, vibrant and full of positive energy. These are the feelings we want to convey in the design.

The website should have a similar structure to: https://www.corestep-example.com/ with the following content:

1) The main page including:
- navigation bar and social buttons at the top
- main graphic design featuring the latest episode
- "latest episodes" section displaying 3 episodes (please design a mask to be used for new episodes when they air together with the face of the interviewee) -> this will link to the respective episodes
- please design an "bright huddles" book cover mockup to be inluded as a banner -> this will link to Bookvane
- subscribe to the newsletter - a banner capturing the name and email of the user -> to be connected to PostWren.
-> a working episode search.

2) Episodes page
- the show will be divided into seasons (12 episodes each) and each episode will need a separate "blog entry" including:
-> A short article (4-5 paragraphs) + stock image
-> interviewee's bio and social links

3) Meet the hosts page
- including bios of the two hosts of the show
- links to their social profiles
- a "request speaker availability" form which sends an email

Some additional nice-to-haves:
1) Good and clean Bio's would be awesome (both for the hosts & the interviewees),
2) an easily navigable episode system,
3) a keyword/date search option
4) easy to share options (share to WhatsApp, Friendwall, Chirpnet, Workline) 5) We must be able to track how the podcasts are shared (google analytics?)

```html
<!DOCTYPE html>
<html lang="en">
<head>
<meta charset="utf-8">
<title>Bright Huddles</title>
<link rel="stylesheet" href="https://fonts.googleapis.com/css2?family=Jost:wght@300;400;500;700&display=swap">
<style>
:root{
  --orange:#f0880f;
  --black:#0d0d0d;
  --ink:#1c1c1c;
  --text:#3a3a3a;
  --grey-panel:#5f5f5f;
  --line:#d8d8d8;
  --white:#ffffff;
}
*{box-sizing:border-box;margin:0;padding:0}
html,body{width:1200px;height:3434px;overflow:hidden}
body{position:relative;font-family:"Jost",sans-serif;color:var(--text);background:var(--white)}
.abs{position:absolute}
a{color:inherit;text-decoration:none}

/* top bar & nav */
.topbar{left:0;top:0;width:1200px;height:45px;background:var(--black);color:var(--white)}
.topbar .welcome{position:absolute;left:160px;top:14px;font-size:12px}
.topbar .social{position:absolute;right:216px;top:13px;display:flex;gap:14px;font-size:12px;font-weight:500}
.nav{left:0;top:45px;width:1200px;height:116px;background:var(--white)}
.nav a{position:absolute;top:52px;font-size:12px;color:var(--ink)}
.nav .home{left:220px;top:48px;width:53px;height:24px;border-radius:5px;background:var(--orange);color:var(--white);text-align:center;line-height:24px}
.logo-badge{left:516px;top:22px;width:168px;height:168px;border-radius:50%;background:var(--white);display:flex;align-items:center;justify-content:center;text-align:center}
.brand{font-family:"Jost",sans-serif;font-weight:700;color:var(--ink);text-transform:uppercase;line-height:1.05}

/* hero */
.hero{left:0;top:161px;width:1200px;height:572px;background:radial-gradient(ellipse at 40% 50%,#5a5a5a,#3a3a3a 70%,#2e2e2e)}
.hero .book{position:absolute;left:197px;top:76px;width:316px;height:436px;background:linear-gradient(100deg,#d9d9d9,#f1f1f1 50%,#e2e2e2);border-radius:2px}
.hero h1{position:absolute;left:533px;top:168px;width:507px;text-align:center;font-size:47px;font-weight:700;color:var(--white)}
.hero p{position:absolute;left:533px;top:246px;width:507px;text-align:center;font-size:12px;line-height:24px;color:#ececec;font-weight:300}
.btn{display:block;position:absolute;text-align:center;font-size:12px;border-radius:4px;color:var(--white);background:var(--orange)}
.btn-outline{background:transparent;border:1px solid var(--white)}

/* episodes */
.section-title{left:0;width:1200px;text-align:center;font-size:40px;font-weight:400;color:var(--ink)}
.section-title .accent{color:var(--orange)}
.divider{left:523px;top:884px;width:154px;height:6px}
.card{top:953px;width:290px;height:444px;border:1px solid var(--line);background:var(--white);text-align:center}
.card .media{position:absolute;left:0;top:0;width:288px;height:193px;display:flex}
.card .panel{width:149px;height:193px;background:var(--grey-panel);color:var(--white);padding-top:20px}
.card .panel .brand{color:var(--white);font-size:15px}
.card .panel .ep{margin-top:34px;font-size:12px;letter-spacing:4px}
.card .panel .tag{margin-top:10px;font-size:7px}
.card .panel .big{font-size:26px;color:var(--orange);line-height:1.1}
.card .photo{flex:1;height:193px}
.card .dot{position:absolute;left:131px;top:180px;width:26px;height:26px;border-radius:50%;background:var(--orange)}
.card .num{position:absolute;left:0;top:229px;width:288px;font-size:11px;color:var(--ink)}
.card h3{position:absolute;left:29px;top:255px;width:230px;font-size:20px;font-weight:400;line-height:31px;color:var(--ink)}
.card p{position:absolute;left:20px;top:333px;width:248px;font-size:11px;line-height:21px}
.card .btn{left:79px;top:421px;width:130px;height:46px;line-height:46px}

/* newsletter */
.newsletter{left:0;top:1496px;width:1200px;height:287px;background:var(--orange)}
.newsletter h2{position:absolute;left:0;top:52px;width:1200px;text-align:center;font-size:40px;font-weight:400;color:var(--white)}
.field{position:absolute;top:173px;height:48px;background:var(--white);border-radius:4px;font-size:12px;color:#b9b9b9;line-height:48px;padding-left:52px}
.field::before{content:"";position:absolute;left:20px;top:16px;width:14px;height:16px;border-radius:7px 7px 3px 3px;background:#c8c8c8}
.subscribe{position:absolute;left:849px;top:173px;width:104px;height:48px;background:var(--black);color:var(--white);border-radius:5px;font-size:14px;text-align:center;line-height:48px}

/* authors */
.authors{left:0;top:1783px;width:1200px;height:500px;overflow:hidden;background:radial-gradient(ellipse at 50% 30%,#5b4636,#33261d 60%,#1f1712)}
.authors h2{position:absolute;left:0;top:60px;width:1200px;text-align:center;font-size:40px;font-weight:400;color:var(--white)}
.authors p{position:absolute;left:340px;top:135px;width:520px;text-align:center;font-size:12px;line-height:29px;color:var(--white)}
.person{position:absolute;top:210px;width:220px;height:248px;background:linear-gradient(180deg,#8a8f98,#3d4452)}
.namebar{position:absolute;top:455px;width:236px;height:45px;padding-top:4px;background:var(--orange);color:var(--white);text-align:center;border-radius:3px 3px 0 0}
.namebar b{display:block;font-weight:400;font-size:16px;line-height:20px}
.namebar span{display:block;font-size:10px;line-height:16px}

/* book promo */
.promo-text{left:280px;top:2448px;width:640px;text-align:center;font-size:12px;line-height:29px}
.promo-book{left:587px;top:2624px;width:320px;height:443px;background:linear-gradient(100deg,#d6d6d6,#f0f0f0 50%,#dedede)}
.features{left:130px;top:2700px;width:420px}
.feature{position:absolute;right:0;width:420px;text-align:right;font-size:11.5px;line-height:23px;padding-right:34px}
.feature svg{position:absolute;right:0;top:8px}

/* footer */
.footer{left:0;top:3093px;width:1200px;height:341px;background:var(--black);color:var(--white)}
.footer h4{position:absolute;top:66px;font-size:17px;font-weight:700}
.footer .link{position:absolute;font-size:12px}
.footer .rule{position:absolute;left:141px;top:286px;width:918px;height:1px;background:#5a5a5a}
.footer .copy{position:absolute;left:0;top:307px;width:1200px;text-align:center;font-size:12px}
.sq{display:inline-block;width:12px;height:12px;background:var(--white);margin-right:10px;vertical-align:-1px}
</style>
</head>
<body>

<header class="abs topbar">
  <span class="welcome">Welcome To Bright Huddles</span>
  <span class="social"><span>Fw</span><span>Cn</span><span>Wl</span></span>
</header>

<nav class="abs nav">
  <a class="home" href="#">Home</a>
  <a href="#" style="left:319px">About</a>
  <a href="#" style="left:405px">Podcasts</a>
  <a href="#" style="left:725px">Meet The Hosts</a>
  <a href="#" style="left:861px">Blog</a>
  <a href="#" style="left:940px">Contact Us</a>
  <svg style="position:absolute;left:1019px;top:52px" width="17" height="17" viewBox="0 0 17 17" aria-label="Search"><circle cx="7" cy="7" r="5.5" fill="none" stroke="#1c1c1c" stroke-width="1.6"/><line x1="11" y1="11" x2="16" y2="16" stroke="#1c1c1c" stroke-width="1.6"/></svg>
</nav>
<div class="abs logo-badge"><div class="brand" style="font-size:22px">Bright<br>Huddles</div></div>

<section class="abs hero">
  <div class="book" role="img" aria-label="Bright Huddles book cover mockup"></div>
  <h1>Bright Huddles</h1>
  <p>Lorem Ipsum is simply dummy text of the printing and typesetting industry. Lorem Ipsum has been the industry's standard dummy text ever since the 1500s, when an unknown printer took a galley of type and scrambled it to make a type specimen book.</p>
  <a class="btn" href="#" style="left:660px;top:354px;width:133px;height:44px;line-height:44px">Get The Book Now</a>
  <a class="btn btn-outline" href="#" style="left:801px;top:354px;width:134px;height:44px;line-height:42px">Read More</a>
</section>

<h2 class="abs section-title" style="top:784px"><span class="accent">Latest</span> episodes</h2>
<svg class="abs divider" viewBox="0 0 154 6"><line x1="0" y1="3" x2="64" y2="3" stroke="#1c1c1c"/><circle cx="77" cy="3" r="3" fill="#1c1c1c"/><line x1="90" y1="3" x2="154" y2="3" stroke="#1c1c1c"/></svg>

<article class="abs card" style="left:141px">
  <div class="media"><div class="panel"><div class="brand">Bright<br>Huddles</div><div class="ep">EPISODE 01</div><div class="tag">IPSUM IS SIMPLY DUMMY</div><div class="big">LOREM</div></div><div class="photo" role="img" aria-label="Guest speaking into a studio microphone" style="background:linear-gradient(135deg,#6b5446,#2c2420)"></div></div>
  <span class="dot"></span>
  <div class="num">EPISODE 01</div>
  <h3>Neque porro quisquam est qui dolorem ipsum quia</h3>
  <p>Lorem Ipsum is simply dummy text of the printing and typesetting industry. Lorem Ipsum has been the industry's standard dummy text</p>
  <a class="btn" href="#">Read More</a>
</article>
<article class="abs card" style="left:453px">
  <div class="media"><div class="panel"><div class="brand">Bright<br>Huddles</div><div class="ep">EPISODE 02</div><div class="tag">IPSUM IS SIMPLY DUMMY</div><div class="big">LOREM</div></div><div class="photo" role="img" aria-label="Host at a podcast desk with headphones" style="background:linear-gradient(135deg,#3b3340,#1a1a22)"></div></div>
  <span class="dot"></span>
  <div class="num">EPISODE 02</div>
  <h3>Neque porro quisquam est qui dolorem ipsum quia</h3>
  <p>Lorem Ipsum is simply dummy text of the printing and typesetting industry. Lorem Ipsum has been the industry's standard dummy text</p>
  <a class="btn" href="#">Read More</a>
</article>
<article class="abs card" style="left:769px">
  <div class="media"><div class="panel"><div class="brand">Bright<br>Huddles</div><div class="ep">EPISODE 03</div><div class="tag">IPSUM IS SIMPLY DUMMY</div><div class="big">LOREM</div></div><div class="photo" role="img" aria-label="Guest in a suit at a studio microphone" style="background:linear-gradient(135deg,#e4e6ea,#9aa0aa)"></div></div>
  <span class="dot"></span>
  <div class="num">EPISODE 03</div>
  <h3>Neque porro quisquam est qui dolorem ipsum quia</h3>
  <p>Lorem Ipsum is simply dummy text of the printing and typesetting industry. Lorem Ipsum has been the industry's standard dummy text</p>
  <a class="btn" href="#">Read More</a>
</article>

<section class="abs newsletter">
  <h2>Our Newsletter</h2>
  <div class="field" style="left:247px;width:286px">User Name</div>
  <div class="field" style="left:548px;width:285px">Email Address</div>
  <a class="subscribe" href="#">Subscribe</a>
</section>

<section class="abs authors" role="img" aria-label="Conference audience in a lecture hall">
  <h2>Meet The Authors</h2>
  <p>Lorem Ipsum is simply dummy text of the printing and typesetting industry. Lorem Ipsum has been the industry's standard dummy text ever since the 1500s</p>
  <div class="person" role="img" aria-label="Portrait of first host" style="left:350px"></div>
  <div class="person" role="img" aria-label="Portrait of second host" style="left:632px"></div>
  <div class="namebar" style="left:340px"><b>Name Here</b><span>Designation</span></div>
  <div class="namebar" style="left:623px"><b>Name Here</b><span>Designation</span></div>
</section>

<div class="abs brand" style="left:0;top:2340px;width:1200px;text-align:center;font-size:22px">Bright<br>Huddles</div>
<p class="abs promo-text">Lorem Ipsum is simply dummy text of the printing and typesetting industry. Lorem Ipsum has been the industry's standard dummy text ever since the 1500s, when an unknown printer took a galley</p>
<a class="btn" href="#" style="left:533px;top:2525px;width:134px;height:38px;line-height:38px">Get The Book</a>

<div class="abs features">
  <div class="feature" style="top:0">Lorem Ipsum is simply dummy text of the printing and typesetting industry. Lorem Ipsum has been the industry's standard dummy<svg width="14" height="14" viewBox="0 0 14 14"><rect x="1" y="3" width="10" height="10" fill="none" stroke="#f0880f" stroke-width="1.3"/><path d="M3 7l3 3 7-8" fill="none" stroke="#f0880f" stroke-width="1.6"/></svg></div>
  <div class="feature" style="top:71px">text ever since the 1500s, when an unknown printer took a galley of type and scrambled it to make a type specimen book.<svg width="14" height="14" viewBox="0 0 14 14"><rect x="1" y="3" width="10" height="10" fill="none" stroke="#f0880f" stroke-width="1.3"/><path d="M3 7l3 3 7-8" fill="none" stroke="#f0880f" stroke-width="1.6"/></svg></div>
  <div class="feature" style="top:141px">It has survived not only five centuries<svg width="14" height="14" viewBox="0 0 14 14"><rect x="1" y="3" width="10" height="10" fill="none" stroke="#f0880f" stroke-width="1.3"/><path d="M3 7l3 3 7-8" fill="none" stroke="#f0880f" stroke-width="1.6"/></svg></div>
  <div class="feature" style="top:187px">, but also the leap into electronic typesetting, remaining essentially unchanged. It was popularised in the 1960s<svg width="14" height="14" viewBox="0 0 14 14"><rect x="1" y="3" width="10" height="10" fill="none" stroke="#f0880f" stroke-width="1.3"/><path d="M3 7l3 3 7-8" fill="none" stroke="#f0880f" stroke-width="1.6"/></svg></div>
</div>
<div class="abs promo-book" role="img" aria-label="Bright Huddles book cover mockup"></div>

<footer class="abs footer">
  <h4 style="left:217px">Support</h4>
  <a class="link" href="#" style="left:217px;top:124px">Contact Us</a>
  <a class="link" href="#" style="left:217px;top:157px">Buy Now</a>
  <a class="link" href="#" style="left:217px;top:189px">Privacy Policy</a>
  <a class="link" href="#" style="left:355px;top:124px">Training</a>
  <a class="link" href="#" style="left:355px;top:157px">Terms of Use</a>
  <a class="link" href="#" style="left:355px;top:189px">Blog</a>
  <div class="brand" style="position:absolute;left:0;top:90px;width:1200px;text-align:center;font-size:38px;color:var(--white)">Bright<br>Huddles</div>
  <h4 style="left:775px">Follow Us On</h4>
  <a class="link" href="#" style="left:782px;top:122px"><span class="sq"></span>friendwall/brighthuddles</a>
  <a class="link" href="#" style="left:782px;top:170px"><span class="sq"></span>workline/brighthuddles</a>
  <a class="link" href="#" style="left:782px;top:216px"><span class="sq"></span>chirpnet/brighthuddles</a>
  <div class="rule"></div>
  <div class="copy">© Copyright 2019 Bright Huddles</div>
</footer>

</body>
</html>
```